A4 Single Page Brochure for Private Cloud Offerings

Theme: Futuristic Tech Company

Brightmoor Systems is looking to offer private cloud services for our enterprise customers in Perth-based data-centres that provides our clients with a lower-cost alternative to Nimbra or KLT yielding better performance.

We are looking for a single A4 brochure with a great graphics design theme to promote these services.

We will be providing five tiers:
- Starter
- Growth
- Professional
- Premier
- Elite

Each plan must list on the brochure the Max VMs, CPU cores, Memory and SSD storage allocated. Refer to the uploaded PNG file.

The brochure must list the following selling points:

- Hosted in a local Perth-based TIER3 and TIER4 datacentres
- WA owned hosting - support local
- Low latency - ultra fast local hosting
- Includes Quorra Host Datacentre licensing
- Includes WallHaven Managed Firewalls for Enterprise level threat detection
- Includes all infrastructure maintenance services
- Full self management of VMs through customer portal
- Includes a 1gbps Internet link
- Predictable fixed monthly fee with no dynamic billing
- No additional charges for Storage Transactions, Internet Usage, VM Snapshots, Datacentre Bandwidth Usage and Firewall Traffic Usage.
- Highly available cluster, no single point of failure.
- Pricing is based on 36 months commit
- Yearly rate increases capped to a maximum of Australian CPI
- All plans have 24/7/365 support with dedicated after hours number.
- Managed backup and managed disaster recovery services can be added to plans

Service provided in accordance with our terms and conditions.

We need the ability to EDIT the brochure to adjust pricing after we receive the final project.

Please do not utilise "Pushing the Boundaries of Technology" - our brand is being replaced with "Specialised Consulting". New website is under development but not launched yet.

Target Market(s)

Information Technology Sector

Colors
0054AA
0677BA
7BADD7
CADEEF
E8F1F8

Requirements
Must have
• Theme of Brightmoor is Blue
Should not have
• Extremely stock imagary that just looks "cheap and stock"

```html
<!DOCTYPE html>
<html lang="en">
<head>
<meta charset="utf-8">
<title>Brightmoor Systems – Private Cloud Brochure</title>
<link rel="stylesheet" href="https://fonts.googleapis.com/css2?family=Outfit:wght@400;500;600;700;800&display=swap">
<style>
:root{
  --navy:#2b2f8a;
  --navy-pill:#3a3f96;
  --teal:#2ff2cf;
  --teal-text:#2ef0c6;
  --ink:#2a2a35;
  --deep:#0d1650;
  --brand-blue:#0054AA;
  --mid-blue:#0677BA;
  --sky:#7BADD7;
  --pale:#CADEEF;
  --mist:#E8F1F8;
  --white:#ffffff;
}
*{margin:0;padding:0;box-sizing:border-box}
html,body{width:849px;height:1200px;overflow:hidden;background:var(--deep)}
body{font-family:"Outfit",sans-serif;color:var(--ink)}
.brochure{position:relative;width:849px;height:1200px;overflow:hidden;
  background:linear-gradient(180deg,#172a86 0%,#1b3e9e 4%,#142a7c 48%,#152a78 60%,#10246a 100%)}
.top-band{position:absolute;left:0;top:0;width:849px;height:56px;
  background:linear-gradient(90deg,#1535a0 0%,#2a58c8 40%,#1a3aa8 70%,#0e2a8a 100%)}
.intro-panel{position:absolute;left:0;top:55px;width:849px;height:523px;
  background:radial-gradient(ellipse at 85% 15%,#d7ecf0 0%,#ffffff 45%),var(--white)}
.intro-panel::after{content:"";position:absolute;left:0;bottom:0;width:100%;height:70px;
  background:linear-gradient(180deg,rgba(255,255,255,0),rgba(202,222,239,.7))}
.intro{position:absolute;left:45px;top:33px;width:342px;font-size:15.3px;line-height:22.8px;color:var(--ink);text-align:justify}
.intro p+p{margin-top:22px}
.brand{position:absolute;left:507px;top:145px;width:240px;display:flex;align-items:center;justify-content:center;gap:10px;
  font-weight:700;font-size:26px;color:var(--navy);letter-spacing:.5px}
.brand-mark{width:18px;height:18px;background:var(--navy)}
.tagline{position:absolute;left:496px;top:212px;font-weight:700;font-size:27px;line-height:36px;color:var(--navy);white-space:nowrap}
.tiers{position:absolute;left:30px;top:348px;width:785px;height:198px;border:1px solid #5a5fa8;background:rgba(255,255,255,.85);z-index:1}
.tiers-tab{position:absolute;left:45px;top:331px;padding:0 14px;height:32px;line-height:32px;border-radius:10px;
  background:var(--navy-pill);color:var(--teal-text);font-weight:700;font-size:17px;z-index:2}
.larger-tab{position:absolute;left:547px;top:534px;width:224px;height:32px;line-height:30px;text-align:center;border-radius:9px;
  background:var(--navy-pill);color:var(--teal-text);font-weight:500;font-size:17px;z-index:2}
.tier-table{position:absolute;left:0;top:0;width:100%;height:100%}
.row-labels{position:absolute;left:17px;top:57px;color:var(--navy);font-weight:700;font-size:16px;line-height:20.5px}
.cost-label{position:absolute;left:17px;top:152px;color:var(--navy);font-size:17px}
.cost-label b{font-weight:700;font-size:16px;margin-left:6px}
.sep{position:absolute;top:39px;width:1px;height:132px;background:#5a5fa8}
.col{position:absolute;top:27px;text-align:right;color:var(--navy)}
.col h3{font-weight:700;font-size:16px;line-height:20px;margin-bottom:8px}
.col .spec{font-size:17px;line-height:22.8px;font-weight:400}
.col .price{margin-top:6px;font-size:17px;font-weight:400;white-space:nowrap}
.features-visual{position:absolute;left:390px;top:640px;width:459px;height:470px;
  background:radial-gradient(ellipse at 45% 35%,rgba(123,173,215,.55) 0%,rgba(6,119,186,.35) 35%,rgba(20,42,124,0) 70%)}
.features-title{position:absolute;left:40px;top:615px;width:759px;height:40px;border-radius:20px;background:var(--teal);
  color:var(--deep);font-weight:700;font-size:21px;line-height:40px;text-align:center;letter-spacing:.2px}
.timeline{position:absolute;left:56px;top:655px;width:2px;height:432px;background:#3c7bdc}
.features{position:absolute;left:83px;top:686px;list-style:none;color:var(--white);font-size:17.8px}
.features li{position:relative;height:27.8px;line-height:27.8px;white-space:nowrap}
.features li.two{height:55.6px}
.features li::before{content:"";position:absolute;left:-31px;top:9px;width:10px;height:10px;border-radius:50%;
  background:#29c8f0;box-shadow:0 0 6px 2px rgba(41,200,240,.6)}
.features .indent{padding-left:10px}
.terms{position:absolute;left:166px;top:1127px;width:511px;height:22px;border-radius:11px;background:var(--teal);
  color:var(--deep);font-size:16.4px;line-height:22px;text-align:center;white-space:nowrap}
</style>
</head>
<body>
<main class="brochure">
  <div class="top-band" role="img" aria-label="Blue circuit-board pattern band"></div>

  <section class="intro-panel">
    <div class="intro">
      <p>Brightmoor Systems is looking to offer private cloud services for our enterprise customers in Perth-based data-centres that provides our clients with a lower-cost alternative to Nimbra or KLT yielding better performance.</p>
      <p>We are looking for a single A4 brochure with a great graphics design theme to promote these services.</p>
    </div>
    <div class="brand"><span class="brand-mark"></span>Brightmoor</div>
    <div class="tagline">"Specialised Consulting"</div>
  </section>

  <div class="tiers-tab">We will be providing five tiers:</div>
  <section class="tiers">
    <div class="tier-table">
      <div class="row-labels">Max VMs<br>CPU cores<br>Memory (GB)<br>SSD storage (TB)</div>
      <div class="cost-label">Monthly <b>Cost</b></div>
      <span class="sep" style="left:171px"></span>
      <span class="sep" style="left:290px"></span>
      <span class="sep" style="left:416px"></span>
      <span class="sep" style="left:548px"></span>
      <span class="sep" style="left:672px"></span>
      <div class="col" style="right:512px"><h3>Starter</h3><div class="spec">5<br>8<br>64<br>3</div><div class="price">$ 1,028.01</div></div>
      <div class="col" style="right:387px"><h3>Growth</h3><div class="spec">10<br>16<br>128<br>8</div><div class="price">$ 3,426.64</div></div>
      <div class="col" style="right:254px"><h3>Professional</h3><div class="spec">15<br>32<br>192<br>15</div><div class="price">$ 4,626.05</div></div>
      <div class="col" style="right:131px"><h3>Premier</h3><div class="spec">20<br>48<br>256<br>20</div><div class="price">$ 5,482.72</div></div>
      <div class="col" style="right:17px"><h3>Elite</h3><div class="spec">25<br>64<br>320<br>30</div><div class="price">$ 7,196.07</div></div>
    </div>
  </section>
  <div class="larger-tab">For larger plans, ask us.</div>

  <div class="features-visual" role="img" aria-label="Glowing data cloud above a team working at computers in a server room"></div>
  <h2 class="features-title">HOSTED IN A LOCAL PERTH-BASED TIER3 AND TIER4 DATA CENTRES</h2>
  <div class="timeline"></div>
  <ul class="features">
    <li>- WA owned hosting - support local</li>
    <li>- Low latency - ultra fast local hosting</li>
    <li>- Includes Quorra Host Datacentre licensing</li>
    <li>- Includes WallHaven Managed Firewalls for Enterprise level threat detection</li>
    <li>- Includes all infrastructure maintenance services</li>
    <li>- Full self management of VMs through customer portal</li>
    <li>- Includes a 1gbps Internet link</li>
    <li>- Predictable fixed monthly fee with no dynamic billing</li>
    <li class="two">- No additional charges for Storage Transactions, Internet Usage,<br><span class="indent">VM Snapshots, Datacentre Bandwidth Usage and Firewall Traffic Usage.</span></li>
    <li>- Highly available cluster, no single point of failure.</li>
    <li>- Pricing is based on 36 months commit</li>
    <li>- Yearly rate increases capped to a maximum of Australian CPI</li>
    <li>- All plans have 24/7/365 support with dedicated after hours number.</li>
    <li>- Managed backup and managed disaster recovery services can be added to plans</li>
  </ul>
  <div class="terms">Service provided in accordance with our terms and conditions.</div>
</main>
</body>
</html>
```